"We Are Hiring" Flyer

I am needing a flyer made for hiring. below is what we would like to have on it as well as our a logo and ive attached a QR code that will link to our jobwick job listing if that can be included as well.
We Are Hiring!
Branch Manager
Starting pay $21-$23 per hour + monthly bonuses + Health Insurance
Reach out to us: info@tallowcrest.com
(about us) Tallowcrest Financial is a different kind of loan company. We understand just how important a loan is to the lives and futures of our clients. Tallowcrest Financial offers flexible payment options and competitive loan rates to ensure that our clients have the best possible experience.
8.5” x 11”
Industry/Entity Type
Finance
Look and feel
Each slider illustrates characteristics of the customer's brand and the style your logo design should communicate.

```html
<!DOCTYPE html>
<html lang="en">
<head>
<meta charset="utf-8">
<title>Tallowcrest Financial – We Are Hiring</title>
<link rel="stylesheet" href="https://fonts.googleapis.com/css2?family=Kaushan+Script&family=Roboto+Condensed:wght@700;900&display=swap">
<style>
  :root {
    --green-bright: #4ff55c;
    --green-mid: #3ee05a;
    --green-lime: #c6f24a;
    --coin-light: #7ff0a0;
    --coin-dark: #2fbf6a;
    --white: #ffffff;
    --gold: #ffd21f;
    --gold-deep: #c98a00;
    --gold-line: #f2b62b;
    --photo-dark: #26282b;
    --photo-mid: #4a4d50;
  }
  html, body { margin: 0; padding: 0; overflow: hidden; }
  body { width: 927px; height: 1200px; }
  .flyer {
    position: relative;
    width: 927px;
    height: 1200px;
    overflow: hidden;
    background:
      radial-gradient(circle at 92% 8%, var(--green-lime) 0%, rgba(198,242,74,0) 38%),
      linear-gradient(160deg, var(--green-bright) 0%, var(--green-mid) 100%);
    font-family: "Roboto Condensed", "Arial Narrow", sans-serif;
    color: var(--white);
  }
  .coin { position: absolute; border-radius: 50%; }
  .coin--top { left: 548px; top: 105px; width: 130px; height: 130px;
    background: radial-gradient(circle at 40% 35%, var(--coin-light), var(--coin-dark)); }
  .coin--corner { left: 770px; top: -20px; width: 170px; height: 170px; opacity: .7;
    background: radial-gradient(circle at 40% 35%, var(--coin-light), var(--coin-dark)); filter: blur(2px); }
  .coin--side { left: 885px; top: 355px; width: 80px; height: 80px;
    background: radial-gradient(circle at 40% 35%, var(--coin-light), var(--coin-dark)); }
  .coin--bottom { left: -70px; top: 910px; width: 320px; height: 320px; opacity: .85;
    background: radial-gradient(circle at 45% 40%, var(--coin-light), var(--coin-dark)); filter: blur(2px); }
  .arrow-shape { position: absolute; left: 520px; top: 340px; width: 170px; height: 140px;
    border-radius: 30px; background: linear-gradient(135deg, #8af59a, #3cc964); opacity: .9; }
  .photo-area {
    position: absolute; left: 440px; top: 120px; width: 487px; height: 1080px;
    background: linear-gradient(160deg, var(--photo-mid) 0%, var(--photo-dark) 60%);
    clip-path: polygon(33% 0, 100% 0, 100% 100%, 0 100%, 0 46%, 33% 46%);
    opacity: .92;
  }
  .zigzag { position: absolute; left: 556px; top: 640px; width: 371px; height: 180px; }
  .brand {
    position: absolute; left: 48px; top: 72px; width: 280px;
    display: flex; align-items: center; gap: 14px;
    font-weight: 700; font-size: 36px; line-height: 1.05; color: var(--white);
  }
  .brand__dot { width: 26px; height: 26px; border-radius: 50%; background: var(--white); flex: none; }
  .hiring {
    position: absolute; left: 48px; top: 226px; margin: 0;
    font-family: "Kaushan Script", cursive; font-weight: 400; font-size: 70px;
    text-shadow: 0 0 18px rgba(255,255,120,.6);
  }
  .role {
    position: absolute; left: 42px; top: 318px; margin: 0;
    font-weight: 900; font-size: 158px; line-height: 140px; letter-spacing: -1px;
    text-shadow: 0 0 22px rgba(255,255,140,.55);
  }
  .pay {
    position: absolute; left: 48px; top: 630px; margin: 0;
    font-weight: 700; font-size: 34px; display: flex; align-items: center; gap: 10px;
  }
  .pay__amount {
    font-weight: 900; font-size: 60px; color: var(--gold);
    -webkit-text-stroke: 2px var(--gold-deep);
    text-shadow: 3px 4px 0 #2f8a2f;
  }
  .perks { position: absolute; left: 46px; top: 724px; margin: 0; padding: 0; list-style: none;
    font-weight: 700; font-size: 36px; line-height: 59px; }
  .contact { position: absolute; left: 50px; top: 1124px; margin: 0; font-weight: 700; font-size: 34px; }
</style>
</head>
<body>
<main class="flyer">
  <div class="coin coin--corner" role="img" aria-label="Green coin with cent sign"></div>
  <div class="coin coin--top" role="img" aria-label="Green coin with cent sign"></div>
  <div class="coin coin--bottom" role="img" aria-label="Large green coin with cent sign"></div>
  <div class="arrow-shape" role="img" aria-label="Green 3D arrow"></div>
  <div class="photo-area" role="img" aria-label="Photo of a smiling branch manager in a dark suit holding a tablet"></div>
  <div class="coin coin--side" role="img" aria-label="Green coin with cent sign"></div>
  <svg class="zigzag" role="img" aria-label="Golden rising zigzag line" viewBox="0 0 371 180">
    <polyline points="0,150 60,110 90,140 170,70 200,100 280,30 310,60 371,20"
      fill="none" stroke="var(--gold-line)" stroke-width="22" stroke-linejoin="round" stroke-linecap="round"/>
  </svg>

  <div class="brand"><span class="brand__dot"></span><span>Tallowcrest Financial</span></div>

  <h2 class="hiring">We Are Hiring!</h2>
  <h1 class="role">Branch<br>Manager</h1>
  <p class="pay">Starting pay <span class="pay__amount">$21-$23</span> /per hour</p>
  <ul class="perks">
    <li>+ monthly bonuses</li>
    <li>+ Health Insurance</li>
  </ul>
  <p class="contact">Reach out to us: info@tallowcrest.com</p>
</main>
</body>
</html>
```